30% Vinegar Modern Simplistic Label

I need a label design for a new company based in Florida called Tallow Meadow. We sell natural cleaning supplies. Our initial product is 30% Vinegar - White Distilled Vinegar is the most common type of vinegar in American households and is made from grain-based ethanol which is converted to acetic acid and diluted to preferred acidity with water. White Distilled Vinegar can be used inside and outside of the home for: cooking, canning, pickling, cleaning, laundry, automotive and gardening needs, to name a few. Our vinegar is naturally derived from corn and has no additives. We would like to see designs that use the color green and portray modern/natural/organic. Very clean, simple designs.

Target Market(s)

Environmental-thinking mother's

Industry/Entity Type

Cleaning Product

Font styles to use
Sans Serif
Script

Colors
00a990
33b8a4
86cfc6
fff3d1
fcf9ce
eaf2ce

Requirements
Must have
• 1 gallon label dimensions
• 11 x 5.5
Nice to have
• I like it to have the same feel as https://www.brivoxmart.example/30-Vinegar-Concentrate-Concentrated-Industrial/dp/K42R19TZQW/ref=sr_1_3?ie=UTF8&qid=1729384756&sr=8-3&keywords=vinegar+30

```html
<!DOCTYPE html>
<html lang="en">
<head>
<meta charset="utf-8">
<title>Tallow Meadow – 30% Vinegar Label</title>
<link rel="stylesheet" href="https://fonts.googleapis.com/css2?family=Cormorant+Garamond:wght@500;600&family=Open+Sans:wght@400&display=swap">
<style>
  :root {
    --page-bg: #f2f2f2;
    --label-bg: #e9edcb;
    --label-edge: #dfe4bd;
    --ink-dark: #2b2b2b;
    --brand-red: #d8222d;
    --teal-soft: #86cfc6;
    --teal-band: #7fc8c0;
    --band-text: #ffffff;
  }
  * { margin: 0; padding: 0; box-sizing: border-box; }
  html, body {
    width: 1200px;
    height: 1000px;
    overflow: hidden;
    background: var(--page-bg);
  }
  .canvas {
    position: relative;
    width: 1200px;
    height: 1000px;
  }
  .label {
    position: absolute;
    left: 360px;
    top: 95px;
    width: 480px;
    height: 810px;
    background: var(--label-bg);
    border: 1px solid var(--label-edge);
    border-radius: 120px / 150px;
  }
  .product-name {
    position: absolute;
    top: 66px;
    left: 0;
    width: 100%;
    text-align: center;
    font-family: "Cormorant Garamond", Georgia, serif;
    font-variant: small-caps;
    font-weight: 600;
    font-size: 40px;
    color: var(--ink-dark);
    letter-spacing: 1px;
  }
  .brand-mark {
    position: absolute;
    left: 196px;
    top: 134px;
    width: 240px;
    height: 260px;
    left: 120px;
    background: var(--teal-soft);
  }
  .brand-name {
    position: absolute;
    top: 418px;
    left: 0;
    width: 100%;
    text-align: center;
    font-family: "Cormorant Garamond", Georgia, serif;
    font-weight: 500;
    font-size: 66px;
    line-height: 62px;
    color: var(--brand-red);
    letter-spacing: 3px;
    text-transform: uppercase;
  }
  .tagline {
    position: absolute;
    left: 83px;
    top: 558px;
    width: 314px;
    height: 30px;
    background: var(--teal-band);
    color: var(--band-text);
    font-family: "Open Sans", Arial, sans-serif;
    font-size: 17px;
    line-height: 30px;
    letter-spacing: 3px;
    text-align: center;
    text-transform: uppercase;
  }
</style>
</head>
<body>
  <main class="canvas">
    <section class="label">
      <h2 class="product-name">30% Vinegar</h2>
      <div class="brand-mark"></div>
      <h1 class="brand-name">Tallow<br>Meadow</h1>
      <p class="tagline">Natural Products</p>
    </section>
  </main>
</body>
</html>
```